New website for Pollard Law Firm at www.keepwinning-example.com

We are a professional law firm located in the Nashville, Tennessee USA area. We focus on personal injury law. We are looking for a slick new website that is user friendly for updating with new blogs, videos, etc. The primary colors should be red, black, and white. It should load extremely fast and have a good mobile component. The pages for the design will include a home page, about us, news, contact us, and practice page. The practice page will be copied for all the practice areas including motor vehicle accidents, slip and fall accidents, dog bites, etc. We have included an image which we would like to include in the new site which shows the color scheme The image is called banner-Car Wreck. The new website should NOT have gavels, court houses, law books, scales or the typical images for a law firm.

Target Market(s)

People in Tennessee involved in accidents

Industry/Entity Type

Legal services, law firm

Coding

Coded - Design and coding required

Number of Pages Required

5+ page

Font styles to use
Serif

Colors
EB3D1F
EC4F4E
F09395
F8D3D4
FCEDEE

Requirements
Should not have
• Gavels, columns, scales, law related images

```html
<!DOCTYPE html>
<html lang="en">
<head>
<meta charset="utf-8">
<title>About Us | Pollard Law Firm</title>
<link rel="stylesheet" href="https://fonts.googleapis.com/css2?family=Playfair+Display:wght@400;700;900&family=Montserrat:wght@400;500;700;800&display=swap">
<style>
:root{
  --ink:#191c22;
  --red:#c1272d;
  --white:#ffffff;
  --text:#2b2d33;
  --muted:#707277;
  --panel:#f3f3f3;
  --line:#c9c9cb;
  --photo-warm:#6b3e24;
}
*{box-sizing:border-box;margin:0;padding:0}
html,body{width:1200px;height:2228px;overflow:hidden;background:var(--white)}
body{position:relative;font-family:"Montserrat",sans-serif;color:var(--text)}
.abs{position:absolute}

/* hero */
.hero-photo{left:0;top:0;width:773px;height:443px;background:linear-gradient(120deg,#3a3c40 0%,#6f7780 38%,#a9b9c6 62%,#dfe8ee 100%)}
.nav-bar{left:656px;top:0;width:544px;height:89px;background:var(--ink)}
.nav{left:700px;top:35px;display:flex;gap:22px;list-style:none}
.nav a{color:var(--white);font-size:13.5px;font-weight:500;text-decoration:none}
.call-btn{left:1066px;top:24px;width:44px;height:41px;background:var(--red);display:flex;align-items:center;justify-content:center}
.brand{left:89px;top:30px;color:var(--white);font-family:"Playfair Display",serif;font-weight:400;line-height:1}
.brand .name{font-size:25px;letter-spacing:.5px}
.brand .sub{font-size:11px;letter-spacing:2px;margin-top:3px;padding-left:26px}
.title-panel{left:773px;top:89px;width:427px;height:307px;background:var(--ink)}
.page-title{left:800px;top:148px;font-family:"Playfair Display",serif;font-weight:700;font-size:84px;line-height:82px;color:var(--white)}
.page-title span{color:var(--red);display:block}

/* intro */
.eyebrow{left:111px;top:556px;font-size:14px;font-weight:700;letter-spacing:3.5px;color:var(--ink)}
.intro-heading{left:89px;top:588px;border-left:3px solid var(--red);padding-left:20px;font-family:"Playfair Display",serif;font-weight:700;font-size:49px;line-height:58px;color:var(--ink);letter-spacing:.6px;white-space:nowrap}
.intro-copy{left:89px;top:733px;width:540px;font-size:12.6px;line-height:19.6px}
.intro-copy p+p{margin-top:21px}
.btn-outline{left:89px;top:996px;width:138px;height:35px;border:1px solid var(--red);color:var(--red);font-size:12.5px;font-weight:700;letter-spacing:3px;display:flex;align-items:center;justify-content:center}
.team-photo{left:655px;top:501px;width:456px;height:586px;background:linear-gradient(150deg,#4a2415 0%,var(--photo-warm) 40%,#3a3a40 75%,#2a2b30 100%)}

/* contact form */
.chat{left:89px;top:1182px;width:1026px;height:667px;background:var(--panel)}
.chat h2{position:absolute;top:58px;width:100%;text-align:center;font-family:"Playfair Display",serif;font-weight:700;font-size:50px;color:var(--ink);letter-spacing:1px}
.chat .lead{position:absolute;left:219px;top:144px;width:588px;text-align:center;font-size:12.6px;line-height:19.6px;color:var(--muted)}
.field{position:absolute;border-bottom:1px solid var(--line);height:34px;font-size:11.5px;color:var(--muted);padding-left:2px}
.submit{position:absolute;left:436px;top:486px;width:151px;height:33px;background:var(--red);color:var(--white);font-size:12.5px;font-weight:700;letter-spacing:3.5px;display:flex;align-items:center;justify-content:center}
.notice{position:absolute;left:263px;top:548px;width:500px;text-align:center;font-size:7.8px;line-height:11.5px;color:#9a9ba0}

/* footer */
.footer{left:0;top:1916px;width:1200px;height:312px;background:var(--ink);color:var(--white)}
.footer-brand{left:89px;top:64px;color:var(--red);font-family:"Playfair Display",serif;font-weight:400;line-height:1}
.footer-brand .name{font-size:38px;letter-spacing:1px}
.footer-brand .sub{font-size:19px;letter-spacing:2px;margin-top:2px;padding-left:40px}
.f-head{font-size:19px;font-weight:800;letter-spacing:-.3px}
.f-list{list-style:none;font-size:12px;line-height:22.5px;margin-top:14px}
.f-list li{display:flex;align-items:flex-start;gap:8px}
.f-list svg{flex:none;margin-top:5px}
.socials{display:flex;gap:12px;margin-top:22px}
.socials span{width:23px;height:23px;border-radius:50%;background:var(--white)}
.rule{left:89px;top:259px;width:1022px;height:1px;background:#3d4048}
.copyright{left:0;top:278px;width:1200px;text-align:center;font-size:11.5px}
</style>
</head>
<body>

<div class="abs hero-photo" role="img" aria-label="Photo of two colleagues reviewing a blue folder beside a laptop in a high-rise office"></div>
<div class="abs nav-bar"></div>
<div class="abs brand"><div class="name">POLLARD</div><div class="sub">LAW FIRM PLLC</div></div>
<ul class="abs nav">
  <li><a href="#">Home</a></li>
  <li><a href="#">About us</a></li>
  <li><a href="#">News</a></li>
  <li><a href="#">Contact us</a></li>
  <li><a href="#">Practice</a></li>
</ul>
<div class="abs call-btn">
  <svg width="16" height="16" viewBox="0 0 24 24" aria-hidden="true"><path fill="#fff" d="M6.6 10.8a15.1 15.1 0 0 0 6.6 6.6l2.2-2.2c.3-.3.7-.4 1-.2 1.1.4 2.3.6 3.6.6.6 0 1 .4 1 1V20c0 .6-.4 1-1 1A17 17 0 0 1 3 4c0-.6.4-1 1-1h3.5c.6 0 1 .4 1 1 0 1.3.2 2.5.6 3.6.1.3 0 .7-.2 1z"/></svg>
</div>
<div class="abs title-panel"></div>
<h1 class="abs page-title">About<span>Us</span></h1>

<div class="abs eyebrow">TRIAL LAWYERS…</div>
<h2 class="abs intro-heading">We are trial lawyers<br>&amp; we are proud of it!</h2>
<div class="abs intro-copy">
  <p>There are many law firms in Tennessee who claim to be trial lawyers, but their attorneys have never seen a courtroom.&nbsp; We have tried hundreds of cases to verdict and we have helped thousands of people in the Tennessee courts.&nbsp; We fight against billion dollar insurance companies, billion dollar corporations, and the State of Tennessee..and we win!</p>
  <p>It is very hard not to take each case personally.&nbsp; Our clients include victims of personal injury who did not ask for the pain from a car wreck; professionals who are trying to provide for their family and save their license; and parents falsely accused in a child custody proceeding.&nbsp; The majority of our clients are referred by other attorneys because they need our specialized expertise.&nbsp; Given what is at stake, we take each client’s matter personally and try to work on each case every day in order to bring justice to our clients.</p>
</div>
<div class="abs btn-outline">OUR TEAM</div>
<div class="abs team-photo" role="img" aria-label="Photo of a trial attorney leaning over a counsel table in a wood-paneled courtroom with a colleague seated behind"></div>

<section class="abs chat">
  <h2>Let's Chat.</h2>
  <p class="lead">Use the form below to contact us regarding your legal inquiry. Please be as detailed as possible. Include the facts of your case and who is involved. To help us best service you, we recommend that you first describe the issue you're having before telling us what you want to achieve. You may also email or call us to make an appointment.</p>
  <div class="field" style="left:196px;top:280px;width:334px">First Name *</div>
  <div class="field" style="left:529px;top:280px;width:0;border:0"></div>
  <div class="field" style="left:529px;top:280px;width:386px;border:0"></div>
  <div class="field" style="left:529px;top:280px;width:334px">Last&nbsp; Name *</div>
  <div class="field" style="left:196px;top:342px;width:719px;margin-left:-1px">Email Address *</div>
  <div class="field" style="left:196px;top:405px;width:719px;height:50px;margin-left:-1px">How Can We Help? *</div>
  <div class="submit">SUBMIT</div>
  <p class="notice">Please do not include confidential or sensitive information in your message. In the event that we are representing a party with opposing interests to your own, we may have a duty to disclose any information you provide to our client.</p>
</section>

<footer class="abs footer">
  <div class="abs footer-brand"><div class="name">POLLARD</div><div class="sub">LAW FIRM PLLC</div></div>
  <div class="abs" style="left:395px;top:66px">
    <div class="f-head">QUICK LINKS</div>
    <ul class="f-list">
      <li>Home</li><li>About us</li><li>News</li><li>Contact us</li><li>Practice</li>
    </ul>
  </div>
  <div class="abs" style="left:596px;top:66px">
    <div class="f-head">CONTACT US</div>
    <ul class="f-list">
      <li><svg width="11" height="13" viewBox="0 0 24 28" aria-hidden="true"><path fill="#fff" d="M12 0a10 10 0 0 0-10 10c0 7 10 18 10 18s10-11 10-18A10 10 0 0 0 12 0zm0 14a4 4 0 1 1 0-8 4 4 0 0 1 0 8z"/></svg><span>1180 Maple Hollow Road | Suite 204<br>&nbsp;| Franklin, TN 37064</span></li>
      <li><svg width="12" height="12" viewBox="0 0 24 24" aria-hidden="true"><path fill="#fff" d="M6.6 10.8a15.1 15.1 0 0 0 6.6 6.6l2.2-2.2c.3-.3.7-.4 1-.2 1.1.4 2.3.6 3.6.6.6 0 1 .4 1 1V20c0 .6-.4 1-1 1A17 17 0 0 1 3 4c0-.6.4-1 1-1h3.5c.6 0 1 .4 1 1 0 1.3.2 2.5.6 3.6.1.3 0 .7-.2 1z"/></svg><span>Phone: (615) 555-0142</span></li>
      <li><svg width="13" height="10" viewBox="0 0 26 20" aria-hidden="true"><path fill="#fff" d="M0 2a2 2 0 0 1 2-2h22a2 2 0 0 1 2 2v1L13 11 0 3zm0 4 13 8 13-8v12a2 2 0 0 1-2 2H2a2 2 0 0 1-2-2z"/></svg><span>Email: office@keepwinning-example.com</span></li>
    </ul>
  </div>
  <div class="abs" style="left:908px;top:66px">
    <div class="f-head">SOCIAL</div>
    <div class="socials"><span></span><span></span><span></span><span></span></div>
  </div>
  <div class="abs rule"></div>
  <div class="abs copyright">©2021 Pollard Law Firm, PLLC.&nbsp; All Rights Reserved.</div>
</footer>

</body>
</html>
```